Business Card Design For A Renovation Contractor Company

We need a business card for a new company based in Singapore, our company name is "KT Planora". We are a renovation contractor that builds designs into reality. We build more of F&B restaurants, retail stores and commercial offices. We work very closely with designers. The final design should communicate to our client that we are a company that you can trust, that will plan and complete your project without giving you a headache. I like my client to remember my company as "KT". The beauty of SIMPLE is important.

Industry/Entity Type

Contractor

Requirements
Nice to have
• Black or Red base

```html
<!DOCTYPE html>
<html lang="en">
<head>
<meta charset="utf-8">
<title>KT Planora – Business Card</title>
<link rel="stylesheet" href="https://fonts.googleapis.com/css2?family=Open+Sans:wght@400;700&display=swap">
<style>
  :root {
    --stage: #e4e2df;
    --card-white: #ffffff;
    --card-black: #000000;
    --brand-red: #e3161b;
    --ink: #111111;
    --text-grey: #6d6d6d;
  }
  * { margin: 0; padding: 0; box-sizing: border-box; }
  html, body { width: 1200px; height: 900px; overflow: hidden; }
  body {
    background: var(--stage);
    font-family: "Open Sans", Arial, sans-serif;
    position: relative;
  }
  .card {
    position: absolute;
    width: 700px;
    height: 400px;
    box-shadow: 0 6px 18px rgba(0,0,0,0.18);
    overflow: hidden;
  }

  /* Back of card */
  .card-back {
    left: 440px;
    top: 50px;
    background: var(--card-black);
  }
  .card-back .brand {
    position: absolute;
    right: 60px;
    top: 140px;
  }
  .brand-row { display: flex; align-items: center; gap: 14px; }
  .brand-dot {
    width: 44px; height: 44px; border-radius: 50%;
    background: var(--brand-red);
    flex: none;
  }
  .brand-name {
    font-weight: 400;
    font-size: 50px;
    line-height: 1;
    letter-spacing: -1px;
    white-space: nowrap;
  }
  .card-back .brand-name { color: var(--card-white); }
  .tagline {
    font-size: 17px;
    margin-top: 6px;
    letter-spacing: 0.2px;
    white-space: nowrap;
  }
  .card-back .tagline { color: var(--card-white); }

  /* Front of card */
  .card-front {
    left: 60px;
    top: 460px;
    background: var(--card-white);
  }
  .card-front .brand {
    position: absolute;
    left: 42px;
    top: 44px;
  }
  .card-front .brand-name { color: var(--ink); font-size: 46px; }
  .card-front .tagline { color: var(--ink); font-size: 16px; }

  .person {
    position: absolute;
    left: 120px;
    top: 262px;
  }
  .person-name {
    color: var(--brand-red);
    font-weight: 700;
    font-size: 22px;
    line-height: 1.2;
  }
  .person-role {
    color: var(--text-grey);
    font-size: 16px;
  }

  .contact {
    position: absolute;
    left: 425px;
    top: 108px;
    color: var(--text-grey);
    font-size: 15px;
    line-height: 1.35;
  }
  .address { margin-bottom: 14px; }
  .address span { display: block; }
  .contact-list { list-style: none; }
  .contact-list li { display: flex; align-items: center; gap: 10px; }
  .contact-list svg { width: 14px; height: 14px; flex: none; }

  .edge-band {
    position: absolute;
    bottom: 0; left: 0; right: 0;
    height: 10px;
    display: flex;
  }
  .edge-band .band-black { background: var(--card-black); flex: 0 0 72%; }
  .edge-band .band-gap { background: var(--card-white); flex: 0 0 4px; }
  .edge-band .band-red { background: var(--brand-red); flex: 1; }
</style>
</head>
<body>

  <section class="card card-back" aria-label="Card back">
    <div class="brand">
      <div class="brand-row">
        <span class="brand-dot"></span>
        <span class="brand-name">KT Planora</span>
      </div>
      <p class="tagline">turning plans into spaces</p>
    </div>
  </section>

  <section class="card card-front" aria-label="Card front">
    <div class="brand">
      <div class="brand-row">
        <span class="brand-dot"></span>
        <span class="brand-name">KT Planora</span>
      </div>
      <p class="tagline">turning plans into spaces</p>
    </div>

    <div class="person">
      <p class="person-name">Marcus Lim</p>
      <p class="person-role">Director</p>
    </div>

    <div class="contact">
      <p class="address">
        <span>Kenanga road #07-2214</span>
        <span>Kenanga Complex</span>
        <span>Singapore 428801</span>
      </p>
      <ul class="contact-list">
        <li>
          <svg viewBox="0 0 14 14" aria-hidden="true"><path d="M1 5c0-2 2-3 6-3s6 1 6 3l-2 1-1-2H4L3 6z M3 7h8l1 5H2z" fill="var(--brand-red)"/></svg>
          318 472 6150 0
        </li>
        <li>
          <svg viewBox="0 0 14 14" aria-hidden="true"><rect x="3" y="1" width="8" height="4" fill="none" stroke="var(--brand-red)" stroke-width="1.4"/><rect x="1" y="5" width="12" height="8" fill="var(--brand-red)"/></svg>
          318 472 6150 7
        </li>
        <li>
          <svg viewBox="0 0 14 14" aria-hidden="true"><rect x="1" y="3" width="12" height="8" fill="none" stroke="var(--brand-red)" stroke-width="1.4"/><path d="M1 3l6 5 6-5" fill="none" stroke="var(--brand-red)" stroke-width="1.4"/></svg>
          marcus@ktplanora.com
        </li>
        <li>
          <svg viewBox="0 0 14 14" aria-hidden="true"><circle cx="7" cy="7" r="6" fill="none" stroke="var(--brand-red)" stroke-width="1.4"/><path d="M1 7h12M7 1c-3 3-3 9 0 12M7 1c3 3 3 9 0 12" fill="none" stroke="var(--brand-red)" stroke-width="1.2"/></svg>
          www.ktplanora.com
        </li>
      </ul>
    </div>

    <div class="edge-band" aria-hidden="true">
      <span class="band-black"></span>
      <span class="band-gap"></span>
      <span class="band-red"></span>
    </div>
  </section>

</body>
</html>
```